Webdesign für Herstellung von Geschenk- und Dekorationsartikeln
Kobalt Prismo ist ein sehr angenehmer und professioneller Designer, der sich viele Gedanken über mein Projekt gemacht hat und ein Design, passend zu meinen Artikeln entworfen hat. Neben einer kompetenten Beratung gab es viele hilfreiche Vorschläge, die über den eigentlichen Auftrag hinaus gingen. Der Designer ist sehr zu empfehlen. Vielen Dank für den freundlichen Kontakt!
Zielgruppe
Wir sind eine kleine Firma, die mit einem Lasergravierer Geschenk- und Dekorationsartikel herstellt, verziert und beschriftet. Hierzu wird hauptsächlich Holz, Papier, Kork, Filz und Glas als Material eingesetzt.
Auch Schmuck , wie z.B. Kettenanhänger und Ohrringe aus Holz werden gefertigt.
Außerdem werden Fotogravur-Arbeiten nach Kundenwunsch angeboten.
Haupt-Zielgruppe sind Frauen ab 30.
Aufgabenstellung
Das Design soll etwas verspielt sein und Freude an den kleinen Dingen des Lebens ausdrücken. Es soll nicht zu sachlich und kühl sein.
Das vorhandene Logo wird bereit gestellt.
Es existiert noch keine Webseite. Die zukünftige Webseite soll über einen Shop verfügen.
Von der Shop-Darstellung her, hat mir die Webseite 'www.qvhauswerk.ch' gefallen.
Es wäre gut, wenn die im Logo vorhandenen Farben auch auf dem Design für die Webseite auftauchen würden.
Als Design-Tool wäre Adobe Photoshop (PSD) für die Erstellung gut.

```html
<!DOCTYPE html>
<html lang="de">
<head>
<meta charset="utf-8">
<title>Lumiora – Lasergravur</title>
<link href="https://fonts.googleapis.com/css2?family=Cormorant+Garamond:ital,wght@0,400;0,500;1,400;1,500&family=Questrial&display=swap" rel="stylesheet">
<style>
:root{
  --paper:#f4f1ee;
  --gold:#b08a55;
  --sand:#d6b98e;
  --ink:#6b6565;
  --ink-soft:#7d7777;
  --line:#dcc8b8;
  --white:#ffffff;
  --serif:"Cormorant Garamond", Georgia, serif;
  --sans:"Questrial", "Helvetica Neue", Arial, sans-serif;
}
*{box-sizing:border-box;margin:0;padding:0}
html,body{width:708px;height:1200px;overflow:hidden;background:var(--paper)}
body{position:relative;font-family:var(--sans);color:var(--ink)}
h1,h2,h3,h4{font-weight:400}
.abs{position:absolute}

/* header */
.nav a{position:absolute;top:29px;font-size:7.5px;color:var(--ink);text-decoration:none;letter-spacing:.2px}
.nav a.active{border-bottom:1px solid var(--ink);padding-bottom:3px}
.brand{position:absolute;display:flex;align-items:center;gap:5px;transform:translateX(-50%);font-family:var(--sans);color:var(--ink);font-size:15px;letter-spacing:.5px}
.brand .dot{width:9px;height:9px;border:1px solid var(--gold);border-radius:50%}

/* hero */
.hero-title{left:81px;top:122px;font-family:var(--serif);font-style:italic;color:var(--gold);font-size:15.5px;letter-spacing:.6px;white-space:nowrap}
.hero-text{left:81px;top:151px;width:232px;font-size:6.6px;line-height:11.2px;color:var(--ink)}
.cta{left:106px;top:208px;width:107px;height:69px;border:1px solid var(--line);border-radius:50%}
.cta-label{left:120px;top:237px;font-size:7.5px;color:var(--ink)}
.cta-arrow{left:190px;top:240px}
.photo{position:absolute}
.photo.ring-tall{left:365px;top:73px;width:127px;height:196px;border-radius:64px/70px;background:radial-gradient(ellipse at 45% 75%,#e2487a 0%,#b81e52 30%,#2d3a25 62%,#0e170f 100%)}
.photo.tube-tall{left:501px;top:119px;width:127px;height:196px;border-radius:64px/70px;background:linear-gradient(135deg,#e8e7e9 0%,#d4d3d6 40%,#c42020 55%,#e9e8ea 75%,#f1f0f1 100%)}

/* about */
.section-title{font-family:var(--serif);font-style:italic;color:var(--gold);font-size:15px;letter-spacing:.8px;white-space:nowrap}
.about-title{left:0;width:708px;top:415px;text-align:center}
.photo.laser{left:83px;top:493px;width:266px;height:154px;border-radius:50%;background:radial-gradient(ellipse at 55% 45%,#c9c6d6 0%,#8a86a6 30%,#6a48d8 60%,#3e2aa0 100%)}
.about-name{left:382px;top:478px;font-family:var(--serif);font-style:italic;color:var(--gold);font-size:10px;letter-spacing:.5px}
.about-text{left:383px;top:498px;width:236px;font-size:6.4px;line-height:11.2px;color:var(--ink)}
.about-text p+p{margin-top:11.2px}

/* products */
.products-title{left:82px;top:756px}
.product{position:absolute;top:802px;width:173px}
.product .photo{position:relative;width:173px;height:116px;background:radial-gradient(ellipse at 45% 90%,#e9538a 0%,#c62a5c 35%,#3b4a33 70%,#111a11 100%)}
.product h3{margin-top:10px;font-family:var(--serif);font-weight:500;font-size:10px;color:var(--ink);letter-spacing:.3px}
.product .price{margin-top:3px;font-family:var(--serif);font-weight:500;font-size:9px;color:var(--ink)}
.product .more{display:inline-flex;align-items:center;gap:4px;margin-top:9px;font-size:8.5px;color:var(--gold);text-decoration:none}
.pager span{position:absolute;border:1px solid var(--ink);border-radius:50%}

/* footer */
.footer-rule{left:0;top:1043px;width:708px;height:1px;background:var(--line)}
.foot-h{position:absolute;top:1082px;font-family:var(--serif);font-size:9.5px;color:var(--ink-soft);letter-spacing:.4px}
.foot-list{position:absolute;top:1103px;list-style:none;font-size:7.5px;line-height:13px;color:var(--ink)}
.foot-note{left:426px;top:1103px;width:190px;font-size:7.5px;line-height:13px;color:var(--ink)}
.newsletter{left:424px;top:1133px;width:202px;height:28px;border-radius:14px;background:var(--white);display:flex;align-items:center}
.newsletter .field{padding-left:14px;flex:1;font-size:8px;color:#b7b1ae}
.newsletter .send{width:64px;height:28px;border-radius:14px;background:var(--sand);color:var(--white);font-size:7.5px;display:flex;align-items:center;justify-content:center}
</style>
</head>
<body>

<nav class="nav">
  <a class="active" style="left:81px" href="#">Home</a>
  <a style="left:120px" href="#">Produkte</a>
  <a style="left:167px" href="#">News</a>
  <a style="left:540px" href="#">Über Uns</a>
  <a style="left:591px" href="#">Kontakt</a>
</nav>
<div class="brand" style="left:351px;top:24px"><span class="dot"></span>Lumiora</div>

<h1 class="abs hero-title">IHRE INDIVIDUALISIERTE GRAVUR</h1>
<p class="abs hero-text">Lorem ipsum dolor sit amet, consectetuer adipiscing elit. Aenean commodo ligula eget dolor. Aenean massa. Cum sociis natoque penatibus et magnis dis parturient montes,</p>
<div class="abs cta"></div>
<span class="abs cta-label">Produktübersicht</span>
<svg class="abs cta-arrow" width="50" height="6" viewBox="0 0 50 6" aria-hidden="true">
  <path d="M0 3 H48 M45 1 L48 3 L45 5" fill="none" stroke="var(--line)" stroke-width=".8"/>
</svg>
<div class="photo ring-tall" role="img" aria-label="Gravierter Ring an einem pinken Band über einer Rosenblüte"></div>
<div class="photo tube-tall" role="img" aria-label="Rote gravierte Metallhülle auf einer weißen Schachtel"></div>

<h2 class="abs section-title about-title">ÜBER UNS</h2>
<div class="photo laser" role="img" aria-label="Lasergravierer bei der Arbeit in violettem Licht"></div>
<h3 class="abs about-name">LUMIORA</h3>
<div class="abs about-text">
  <p>Lorem ipsum dolor sit amet, consectetuer adipiscing elit. Aenean commodo ligula eget dolor. Aenean massa. Cum sociis natoque penatibus et magnis dis parturient montes, nascetur ridiculus mus. Donec quam felis, ultricies nec, pellentesque eu, pretium quis, sem. Nulla consequat massa quis enim. Donec pede justo, fringilla vel, aliquet nec, vulputate eget, arcu. In enim justo, rhoncus ut,</p>
  <p>imperdiet a, venenatis vitae, justo. Nullam dictum felis eu pede mollis pretium. Integer tincidunt. Cras dapibus. Vivamus elementum semper nisi. Aenean vulputate eleifend tellus.</p>
  <p>Aenean leo ligula, porttitor eu, consequat vitae, eleifend ac, enim. Aliquam lorem ante, dapibus in, viverra quis, feugiat a, tellus. Phasellus viverra nulla ut metus varius laoreet. Quisque rutrum.</p>
</div>

<h2 class="abs section-title products-title">UNSERE PRODUKTE</h2>

<article class="product" style="left:81px">
  <div class="photo" role="img" aria-label="Gravierter Ring über einer pinken Rose"></div>
  <h3>GRAVIERTE RINGE</h3>
  <div class="price">3.33€</div>
  <a class="more" href="#">ansehen <svg width="7" height="6" viewBox="0 0 7 6"><path d="M0 3 H6 M3.5 .5 L6 3 L3.5 5.5" fill="none" stroke="var(--gold)" stroke-width="1.1"/></svg></a>
</article>
<article class="product" style="left:267px">
  <div class="photo" role="img" aria-label="Gravierter Ring über einer pinken Rose"></div>
  <h3>GRAVIERTE RINGE</h3>
  <div class="price">3.33€</div>
  <a class="more" href="#">ansehen <svg width="7" height="6" viewBox="0 0 7 6"><path d="M0 3 H6 M3.5 .5 L6 3 L3.5 5.5" fill="none" stroke="var(--gold)" stroke-width="1.1"/></svg></a>
</article>
<article class="product" style="left:454px">
  <div class="photo" role="img" aria-label="Gravierter Ring über einer pinken Rose"></div>
  <h3>GRAVIERTE RINGE</h3>
  <div class="price">3.33€</div>
  <a class="more" href="#">ansehen <svg width="7" height="6" viewBox="0 0 7 6"><path d="M0 3 H6 M3.5 .5 L6 3 L3.5 5.5" fill="none" stroke="var(--gold)" stroke-width="1.1"/></svg></a>
</article>

<div class="pager">
  <span style="left:328px;top:1004px;width:14px;height:14px"></span>
  <span style="left:351px;top:1006px;width:9px;height:9px"></span>
  <span style="left:370px;top:1006px;width:9px;height:9px"></span>
</div>

<div class="abs footer-rule"></div>
<footer>
  <h4 class="foot-h" style="left:79px">SITEMAP</h4>
  <ul class="foot-list" style="left:80px"><li>Home</li><li>Über Uns</li><li>Produkte</li><li>News</li></ul>
  <h4 class="foot-h" style="left:171px">KONTAKT</h4>
  <ul class="foot-list" style="left:173px"><li>Kontakt</li><li>Impressum</li><li>AGB</li><li>Datenschutz</li></ul>
  <div class="brand" style="left:347px;top:1110px"><span class="dot"></span>Lumiora</div>
  <h4 class="foot-h" style="left:426px">KONTAKTIEREN SIE UNS</h4>
  <p class="abs foot-note">Wenn Sie weitere Fragen haben hinterlassen Sie uns Ihre E-Mail.</p>
  <div class="abs newsletter"><span class="field">E-mail</span><span class="send">Absenden</span></div>
</footer>

</body>
</html>
```